Australian residential property business needs a business card design

I need a business card design for my new business 'Meadow Estate Partners'. The business will involve house purchases, land development sites, renovation projects, sub-divisions etc. I will be buying property from motivated vendors and working with property investors. I will deal with a wide range of people working in the residential property market including real estate agents, councils, tradespeople, banks, home owners, etc.

I would like something simple, not flashy, but a little bit unique. The colours should be in line with my logo. The business card needs to be professional. I would like something memorable, but not 'busy' or too bright. Not boring. Modern ok.

Target Market(s)

Home owners looking to sell their property, real estate agents, tradespeople (e.g. plumbers, builders, electricians etc), property investors, local councils, and anyone else involved in the residential property industry

Industry/Entity Type

Business

Contact Information for Business Card

I need to include my business name/logo, my name, my title, a PO Box number/address, a mobile number, and an email address.

Font styles to use
Serif

Requirements
Must have
• My business card details listed above.

```html
<!DOCTYPE html>
<html lang="en">
<head>
<meta charset="utf-8">
<title>Meadow Estate Partners — Business Card</title>
<link rel="stylesheet" href="https://fonts.googleapis.com/css2?family=Arimo:wght@700&family=Open+Sans:wght@400;600&display=swap">
<style>
  :root {
    --backdrop: #8e8e8e;
    --card-white: #ffffff;
    --brand-orange: #ee8820;
    --brand-orange-deep: #e27d17;
    --brand-yellow: #f8cb33;
    --ink: #2b2b2b;
    --accent-green: #3f9a3a;
  }
  * { margin: 0; padding: 0; box-sizing: border-box; }
  html, body {
    width: 1200px; height: 900px; overflow: hidden;
    background: var(--backdrop);
  }
  .canvas {
    position: relative; width: 1200px; height: 900px;
  }
  .card {
    position: absolute; left: 320px; width: 560px; height: 320px;
    box-shadow: 0 6px 18px rgba(0,0,0,0.25);
    overflow: hidden;
  }
  /* Card back */
  .card--back {
    top: 90px;
    background: var(--brand-orange-deep);
    display: flex; flex-direction: column; align-items: center; justify-content: center;
    color: #fff;
    font-family: "Arimo", Arial, sans-serif;
  }
  .back-title {
    font-size: 24px; font-weight: 700; letter-spacing: 0.5px; line-height: 1;
  }
  .back-subtitle {
    font-size: 15px; font-weight: 700; letter-spacing: 6px; margin-top: 2px; line-height: 1;
  }
  /* Card front */
  .card--front {
    top: 470px;
    background: var(--card-white);
    font-family: "Open Sans", Arial, sans-serif;
    color: var(--ink);
  }
  .card-graphics {
    position: absolute; inset: 0; width: 560px; height: 320px;
  }
  .holder {
    position: absolute; left: 52px; top: 20px;
  }
  .holder-name {
    font-size: 21px; font-weight: 600; color: var(--brand-orange); line-height: 1.1;
  }
  .holder-title {
    font-size: 14px; line-height: 1.3;
  }
  .contact {
    position: absolute; left: 42px; top: 150px;
    font-size: 14px; line-height: 1.4;
  }
  .contact-label { color: var(--brand-orange); }
  .address { margin-top: 8px; font-size: 15px; line-height: 1.3; }
  .brand-mark {
    position: absolute; left: 330px; top: 150px;
    display: flex; align-items: center; gap: 8px;
  }
  .brand-square {
    width: 16px; height: 16px; background: var(--accent-green);
  }
  .brand-name {
    font-family: "Open Sans", Arial, sans-serif;
    font-size: 17px; font-weight: 600; color: var(--brand-orange);
  }
</style>
</head>
<body>
<main class="canvas">
  <section class="card card--back">
    <div class="back-title">MEADOW ESTATE</div>
    <div class="back-subtitle">Partners</div>
  </section>

  <section class="card card--front">
    <svg class="card-graphics" viewBox="0 0 560 320" aria-hidden="true">
      <polygon points="0,14 26,14 0,52" fill="var(--brand-orange)"/>
      <polygon points="30,14 44,14 18,52 4,52" fill="var(--brand-yellow)"/>
      <polygon points="0,278 300,278 292,292 0,292" fill="var(--brand-yellow)"/>
      <polygon points="306,278 560,278 560,320 280,320" fill="var(--brand-orange)"/>
    </svg>

    <div class="holder">
      <div class="holder-name">Daniel Harper</div>
      <div class="holder-title">Managing Director</div>
    </div>

    <div class="contact">
      <div><span class="contact-label">p:</span> 044-987 654 321</div>
      <div><span class="contact-label">e:</span> hello@meadowestate.com</div>
      <div class="address">12345, Address Goes Here<br>Country Name, 123456</div>
    </div>

    <div class="brand-mark">
      <span class="brand-square"></span>
      <span class="brand-name">Meadow Estate Partners</span>
    </div>
  </section>
</main>
</body>
</html>
```